Simple, Professional and neat business card design for Vendralo Inc.

We're looking to re-vamp our business card design. We're a supplier of innovative feed ingredients for the North American animal agriculture industry. We are located in Lucknow, Ontario, Canada and our flagship product is a product that prevents milk fever in dairy cows when the calve, it is fed before calving and is very effective compared to other alternatives available on the market today.

Our company has Danish roots and we import all of our product from our Danish partner/manufacturer in Denmark. We like our design to embrace high professionalism while remaining neat and simple.

Target Market(s)

B2B, Feed Mills, Veterinary Clinics, Large integrators/producers,

Industry/Entity Type

Agribusiness

Contact Information for Business Card

We like the rounded corners because they make the card easy to sit in a wallet and not many use it so it makes the card stand out, just possibly something to take account for during the design.

As you can also see on the sliders below, looking for a that simple but proffesional scandinavian design.

Requirements
Nice to have
• Rounded corners
Should not have
• Too vibrant

```html
<!DOCTYPE html>
<html lang="en">
<head>
<meta charset="utf-8">
<title>Vendralo Inc. — Business Card</title>
<link rel="stylesheet" href="https://fonts.googleapis.com/css2?family=Open+Sans:wght@400;800&display=swap">
<style>
  :root {
    --backdrop: #2b3238;
    --card-front: #eef2e8;
    --card-back: #b5bdad;
    --band: #3a4048;
    --brand-blue: #1e4fd8;
    --ink: #f3f5ef;
    --rule: #4a5048;
    --mark-gold: #c9a65a;
  }
  * { box-sizing: border-box; margin: 0; padding: 0; }
  html, body { width: 1200px; height: 1200px; overflow: hidden; }
  body {
    background: var(--backdrop);
    font-family: "Open Sans", Arial, sans-serif;
    position: relative;
  }
  .card {
    position: absolute;
    left: 170px;
    width: 860px;
    height: 491px;
    border-radius: 44px;
    overflow: hidden;
  }
  /* Front */
  .card--front {
    top: 70px;
    background: var(--card-front);
  }
  .front-brand {
    position: absolute;
    left: 0; right: 0; top: 170px;
    display: flex; align-items: center; justify-content: center; gap: 26px;
  }
  .brand-mark {
    width: 70px; height: 70px;
    border-radius: 50%;
    background: var(--mark-gold);
    flex: none;
  }
  .brand-name {
    font-weight: 800;
    color: var(--brand-blue);
    font-size: 64px;
    letter-spacing: 1px;
    text-transform: uppercase;
  }
  .front-web {
    position: absolute;
    left: 0; right: 0; top: 300px;
    text-align: center;
    color: var(--brand-blue);
    font-size: 22px;
    letter-spacing: 1px;
  }
  /* Back */
  .card--back {
    top: 620px;
    background: var(--card-back);
  }
  .back-brand {
    position: absolute;
    left: 40px; top: 140px; width: 360px;
    display: flex; flex-direction: column; align-items: center; gap: 22px;
  }
  .back-brand .brand-mark { width: 90px; height: 90px; }
  .back-brand .brand-name { font-size: 44px; }
  .divider {
    position: absolute;
    left: 420px; top: 80px;
    width: 2px; height: 300px;
    background: var(--rule);
  }
  .social {
    position: absolute;
    right: 40px; top: 30px;
    display: flex; gap: 12px;
  }
  .social span {
    width: 22px; height: 22px; border-radius: 50%;
    background: var(--brand-blue); opacity: .6;
  }
  .contact {
    position: absolute;
    left: 450px; top: 80px;
    color: var(--ink);
    font-size: 20px;
    line-height: 1.45;
  }
  .contact__name { color: var(--brand-blue); font-size: 32px; line-height: 1.2; }
  .contact__role { margin-bottom: 4px; }
  .contact__row { display: flex; align-items: center; gap: 12px; }
  .contact__row svg { width: 22px; height: 22px; flex: none; }
  .contact__link { color: var(--brand-blue); }
  .band {
    position: absolute;
    left: 0; right: 0; bottom: 0; height: 56px;
    background: var(--band);
    display: flex; align-items: center; gap: 14px;
    padding-left: 70px;
    color: var(--ink);
    font-size: 20px;
  }
  .band svg { width: 22px; height: 22px; }
</style>
</head>
<body>
  <section class="card card--front">
    <div class="front-brand">
      <span class="brand-mark"></span>
      <span class="brand-name">Vendralo Inc.</span>
    </div>
    <p class="front-web">www.info@vendralo.com</p>
  </section>

  <section class="card card--back">
    <div class="social"><span></span><span></span><span></span></div>
    <div class="back-brand">
      <span class="brand-mark"></span>
      <span class="brand-name">Vendralo Inc.</span>
    </div>
    <div class="divider"></div>
    <div class="contact">
      <p class="contact__name">Mikkel Rasmussen</p>
      <p class="contact__role">CEO</p>
      <p>88 Ridgeway Street, Alderbrook,</p>
      <p>ON, Canada</p>
      <p class="contact__row">
        <svg viewBox="0 0 24 24" fill="none" stroke="#1e4fd8" stroke-width="2"><path d="M5 3h4l2 5-3 2a12 12 0 0 0 6 6l2-3 5 2v4a2 2 0 0 1-2 2A18 18 0 0 1 3 5a2 2 0 0 1 2-2z"/></svg>
        555.201.4410</p>
      <p class="contact__row">
        <svg viewBox="0 0 24 24" fill="#1e4fd8"><rect x="6" y="2" width="12" height="6"/><rect x="2" y="9" width="20" height="9" rx="2"/><rect x="6" y="15" width="12" height="7" fill="#e0e4da"/></svg>
        555-201-4499</p>
      <p class="contact__row">
        <svg viewBox="0 0 24 24" fill="#1e4fd8"><path d="M2 5h20v14H2z"/><path d="M2 5l10 8 10-8" stroke="#e0e4da" stroke-width="2" fill="none"/></svg>
        mikkel@vendralo.com</p>
      <p class="contact__row contact__link">
        <svg viewBox="0 0 24 24" fill="none" stroke="#1e4fd8" stroke-width="2"><circle cx="12" cy="12" r="10"/><path d="M2 12h20M12 2c3 3 3 17 0 20M12 2c-3 3-3 17 0 20"/></svg>
        info@vendralo.com</p>
    </div>
    <div class="band">
      <svg viewBox="0 0 24 24" fill="#1e4fd8"><path d="M5 3h4l2 5-3 2a12 12 0 0 0 6 6l2-3 5 2v4a2 2 0 0 1-2 2A18 18 0 0 1 3 5a2 2 0 0 1 2-2z"/></svg>
      <span>555-307-0120 - 800-555-0187</span>
    </div>
  </section>
</body>
</html>
```